Design of Stationery (Business Card, Letterhead and Envelope) for Investment Company
Kestrelmoor Capital Associates Limited
Design of Stationery (Business Card, Letterhead and Envelope) for Investment Company - Financial Services
Creative Brief
Simple
Tunde A. Ibekwe
Director
7C, Dunmore Crescent, Osapa Garden Estate, Lekki Peninsula, Lagos
tunde@kestrelmoorng.example
www.kestrelmoorng.example
RC 458290
The back of the business card should have the logo of the company on navy blue background - please see the logo uploaded. Below the logo should be the words: "INVESTMENTS. ADVICE. VALUE CREATION".

```html
<!DOCTYPE html>
<html lang="en">
<head>
<meta charset="utf-8">
<title>Kestrelmoor Capital Associates – Business Card</title>
<link href="https://fonts.googleapis.com/css2?family=Montserrat:wght@400;500&display=swap" rel="stylesheet">
<style>
  :root {
    --stage: #e9eaed;
    --paper: #ffffff;
    --navy: #3a4f7a;
    --navy-deep: #2c3d63;
    --silver: #b4b8bf;
    --silver-light: #dfe1e5;
    --ink: #2f3a52;
    --ink-soft: #5b6375;
  }
  * { box-sizing: border-box; margin: 0; padding: 0; }
  html, body {
    width: 1200px; height: 901px; overflow: hidden;
    background: var(--stage);
    font-family: "Montserrat", Arial, sans-serif;
  }
  .business-card {
    position: absolute; left: 150px; top: 190px;
    width: 900px; height: 520px;
    background: var(--paper);
    border-radius: 30px;
    overflow: hidden;
    box-shadow: 0 18px 40px rgba(30, 40, 60, 0.18);
  }
  .card-shapes { position: absolute; inset: 0; width: 900px; height: 520px; }
  .brand {
    position: absolute; left: 70px; top: 60px;
    width: 320px;
    display: flex; flex-direction: column; align-items: center;
  }
  .brand-square {
    width: 60px; height: 60px; background: var(--navy);
    border-radius: 6px; margin-bottom: 18px;
  }
  .brand-name {
    font-weight: 500; color: var(--navy);
    font-size: 24px; letter-spacing: 3px; line-height: 1.3;
    text-transform: uppercase; text-align: center;
  }
  .holder { position: absolute; left: 560px; top: 48px; }
  .holder-name {
    font-size: 20px; font-weight: 500; letter-spacing: 1.5px;
    color: var(--ink); text-transform: uppercase;
  }
  .holder-role { font-size: 14px; color: var(--ink-soft); margin-top: 4px; }
  .contact-list { position: absolute; left: 560px; top: 118px; list-style: none; }
  .contact-list li {
    display: flex; align-items: center; gap: 14px;
    font-size: 14px; color: var(--ink-soft); height: 28px; white-space: nowrap;
  }
  .contact-list svg { width: 15px; height: 15px; fill: var(--ink); flex: none; }
  .address {
    position: absolute; left: 60px; top: 405px;
    color: #ffffff; font-size: 22px; line-height: 1.45;
  }
</style>
</head>
<body>
  <div class="business-card">
    <svg class="card-shapes" viewBox="0 0 900 520" aria-hidden="true">
      <defs>
        <linearGradient id="silverFade" x1="0" y1="0" x2="1" y2="0">
          <stop offset="0" stop-color="#dfe1e5"/>
          <stop offset="1" stop-color="#b4b8bf"/>
        </linearGradient>
      </defs>
      <path d="M0,300 C300,250 600,345 900,272 L900,318 C600,392 300,300 0,342 Z" fill="url(#silverFade)"/>
      <path d="M0,342 C300,300 600,392 900,318 L900,520 L0,520 Z" fill="#3a4f7a"/>
      <path d="M0,356 C300,316 600,408 900,334" fill="none" stroke="#2c3d63" stroke-width="3" opacity="0.5"/>
    </svg>

    <div class="brand">
      <div class="brand-square"></div>
      <div class="brand-name">Kestrelmoor<br>Capital Associates</div>
    </div>

    <div class="holder">
      <div class="holder-name">Tunde A. Ibekwe</div>
      <div class="holder-role">Managing Director</div>
    </div>

    <ul class="contact-list">
      <li><svg viewBox="0 0 16 16"><path d="M4 1l3 3-2 2c1 2 3 4 5 5l2-2 3 3-2 3C7 15 1 9 1 3z"/></svg>012 480 3157</li>
      <li><svg viewBox="0 0 16 16"><rect x="4" y="1" width="8" height="14" rx="1.5"/></svg>012 480 3158</li>
      <li><svg viewBox="0 0 16 16"><rect x="1" y="6" width="14" height="7" rx="1"/><rect x="4" y="2" width="8" height="4"/></svg>012 480 3159</li>
      <li><svg viewBox="0 0 16 16"><path d="M1 3h14v10H1z"/><path d="M1 3l7 6 7-6" fill="none" stroke="#fff" stroke-width="1.2"/></svg>tunde@kestrelmoorng.example</li>
      <li><svg viewBox="0 0 16 16"><circle cx="8" cy="8" r="7"/></svg>www.kestrelmoorng.example</li>
    </ul>

    <div class="address">7C, Dunmore Crescent<br>Osapa Garden Estate, Lagos</div>
  </div>
</body>
</html>
```